Improving a camping website homepage header*

My client is very happy with his new website and its new functionalities. However, he's not very happy about the homepage design. Specifically, the header(this includes the menu, large header image and two columns beneath that). You can find the website here: http://lnkvo.example/siteTentra .

He forwarded me several other websites he likes. Which can be found in the attachments. I also included several pictures of the camping.

I'm looking for a design that will improve the header of the homepage with room for other global style chances. The logo cannot be changed.

Attachments
1) His old website homepage
2) Website mockup he liked.
3) Another website mockup he liked.

Other images can be found on the new website http://lnkvo.example/siteTentra or his old website http://lnkvo.example/formerSiteTentra.

Can you help us?
Updates

Hello guys. Here's a bit more information - Language used on the website is dutch. - The two columns left/right are supposed to link to Hire/Buy chalets. The client indicated that he finds these links important, but doesn't like the current design. I think this is partially the case because he doesn't like the icons. I'm looking forward to your designs!

Target Market(s)

30-50 year old wealthy people that want to purchase or rent cabins in the Netherlands.

Number of Pages Required

1 page

Colors

Designer to choose colors to be used in the design.

Requirements
Must have
• Improved header
Nice to have
• Global style changes
Should not have
• Logo changes

```html
<!DOCTYPE html>
<html lang="nl">
<head>
<meta charset="utf-8">
<title>Parc Lindewaard</title>
<link rel="stylesheet" href="https://fonts.googleapis.com/css2?family=Open+Sans:wght@400;600;700&display=swap">
<style>
:root{
  --green:#7ab51d;
  --green-dark:#5e9312;
  --orange:#f39200;
  --grey-band:#d9d9d9;
  --grey-card:#ffffff;
  --text:#333333;
  --white:#ffffff;
  --photo-sky:#b9c9d6;
  --photo-green:#6f8f52;
}
*{box-sizing:border-box;margin:0;padding:0}
html,body{width:826px;height:1200px;overflow:hidden}
body{font-family:"Open Sans",Arial,sans-serif;color:var(--text);background:var(--white);font-size:12px}
.site{width:826px;height:1200px;position:relative}

/* header */
.site-header{height:82px;display:flex;align-items:center;justify-content:space-between;padding:0 56px}
.brand{display:flex;align-items:center;gap:10px}
.brand-mark{width:34px;height:34px;border-radius:50%;background:var(--green)}
.brand-name{font-size:26px;font-weight:600;color:var(--green);line-height:1}
.brand-sub{font-size:10px;color:var(--green);display:block;margin-top:2px}
.phone{display:flex;align-items:center;gap:10px;font-size:22px;color:var(--green);font-weight:600}
.phone-dot{width:34px;height:34px;border-radius:50%;background:var(--green);display:flex;align-items:center;justify-content:center}

/* nav */
.main-nav{height:34px;background:var(--green);display:flex;align-items:center;padding-left:56px;position:relative}
.main-nav a{color:var(--white);text-decoration:none;font-size:14px;margin-right:26px}
.login{position:absolute;right:56px;top:0;height:34px;width:100px;background:var(--orange);color:var(--white);display:flex;align-items:center;justify-content:center;font-size:14px}

/* hero */
.hero{margin:0 53px;height:266px;background:linear-gradient(180deg,var(--photo-sky) 0%,#8ea98a 35%,var(--photo-green) 65%,#5d7f66 100%)}

/* content */
.content{position:absolute;left:53px;top:388px;width:720px;height:672px;background:var(--grey-band);padding:10px;display:flex;gap:12px}
.posts{width:534px}
.post{margin-bottom:8px}
.post-title{display:flex;align-items:center;gap:8px;height:28px;color:var(--green);font-size:19px;font-weight:700}
.post-title .icon{width:18px;height:18px;background:var(--green)}
.post-card{background:var(--grey-card);height:178px;padding:10px;display:flex;gap:12px}
.post-photo{width:300px;height:158px}
.post-photo.chalet-rent{background:linear-gradient(180deg,#c9d4dc 0%,#e6e3dc 45%,#7c9a58 100%)}
.post-photo.chalet-buy{background:linear-gradient(180deg,#a9b98f 0%,#dfe0d6 50%,#6f8f4a 100%)}
.post-photo.park{background:linear-gradient(180deg,#aebfcd 0%,#7f9b80 50%,#5c7c8c 100%)}
.post-body{flex:1;position:relative;font-size:12.5px;line-height:1.35}
.btn{position:absolute;right:0;bottom:0;background:var(--green);color:var(--white);font-size:12px;padding:8px 16px}

.sidebar{width:154px;display:flex;flex-direction:column}
.sidebar-head{background:var(--green);color:var(--white);height:32px;display:flex;align-items:center;justify-content:center;font-size:15px;margin-bottom:8px}
.thumb{margin:0 auto 12px;width:116px}
.thumb-photo{height:104px;background:linear-gradient(180deg,#c4d0d8 0%,#d9d6cd 45%,#6e8e50 100%)}
.thumb-label{background:var(--green);color:var(--white);font-size:9px;text-align:center;width:56px;margin:2px auto 0;padding:1px 0}
.pager{display:flex;justify-content:space-between;margin-top:auto}
.pager span{background:var(--green);color:var(--white);width:34px;height:28px;display:flex;align-items:center;justify-content:center;font-size:13px;font-weight:700}

/* footer */
.site-footer{position:absolute;left:0;top:1068px;width:826px;height:132px;background:var(--green);color:var(--white);padding:22px 56px}
.contact-line{display:flex;align-items:center;gap:8px;font-size:13px;margin-bottom:8px}
.social{position:absolute;left:606px;top:28px;display:flex;gap:10px}
.social span{width:28px;height:28px;border:3px solid var(--white);border-radius:5px}
.copyright{position:absolute;right:56px;bottom:16px;font-size:13px}
</style>
</head>
<body>
<div class="site">
  <header class="site-header">
    <div class="brand">
      <span class="brand-mark"></span>
      <div><span class="brand-name">Parc Lindewaard</span><span class="brand-sub">Huur &amp; Koop</span></div>
    </div>
    <div class="phone">
      <span class="phone-dot"><svg width="18" height="18" viewBox="0 0 24 24"><path fill="#fff" d="M6.6 10.8a15 15 0 0 0 6.6 6.6l2.2-2.2c.3-.3.7-.4 1-.2 1.1.4 2.3.6 3.6.6.6 0 1 .4 1 1V20c0 .6-.4 1-1 1C10.6 21 3 13.4 3 4c0-.6.4-1 1-1h3.5c.6 0 1 .4 1 1 0 1.3.2 2.5.6 3.6.1.3 0 .7-.2 1z"/></svg></span>
      0123 - 45 67 89
    </div>
  </header>

  <nav class="main-nav">
    <a>Home</a><a>Het Park</a><a>Financiering</a><a>Chalets</a><a>Aanbiedingen</a><a>Faciliteiten</a><a>Contact</a>
    <span class="login">Inloggen</span>
  </nav>

  <div class="hero" role="img" aria-label="Luchtfoto van het chaletpark aan het water"></div>

  <main class="content">
    <div class="posts">
      <article class="post">
        <h2 class="post-title"><span class="icon"></span>Chalet huren</h2>
        <div class="post-card">
          <div class="post-photo chalet-rent" role="img" aria-label="Foto van een huurchalet met tuin"></div>
          <div class="post-body">Huurchalets met 1, 2 &amp; 3 slaapkamers van standaard tot luxe in uitvoering en lokatie.<span class="btn">Lees verder</span></div>
        </div>
      </article>
      <article class="post">
        <h2 class="post-title"><span class="icon"></span>Chalet kopen</h2>
        <div class="post-card">
          <div class="post-photo chalet-buy" role="img" aria-label="Foto van een chalet te koop"></div>
          <div class="post-body">Lorem ipsum dolor sit amet, consectetur adipiscing elit. Aenean euismod bibendum laoreet. Proin gravida dolor sit amet lacus accumsan et viverra justo commodo.<span class="btn">Lees verder</span></div>
        </div>
      </article>
      <article class="post">
        <h2 class="post-title"><span class="icon"></span>Het Park</h2>
        <div class="post-card">
          <div class="post-photo park" role="img" aria-label="Luchtfoto van het park met chalets aan het water"></div>
          <div class="post-body">Nog geen 20 km van Utrecht ligt Recreatiepark Lindewaard. De gunstige ligging maakt het park tot een uniek recreatiegebied.<span class="btn">Lees verder</span></div>
        </div>
      </article>
    </div>

    <aside class="sidebar">
      <div class="sidebar-head">Meer berichten</div>
      <div class="thumb"><div class="thumb-photo" role="img" aria-label="Foto van een chalet"></div><div class="thumb-label">Kavel 3</div></div>
      <div class="thumb"><div class="thumb-photo" role="img" aria-label="Foto van een chalet"></div><div class="thumb-label">Kavel 15</div></div>
      <div class="thumb"><div class="thumb-photo" role="img" aria-label="Foto van een chalet"></div><div class="thumb-label">Kavel 17</div></div>
      <div class="thumb"><div class="thumb-photo" role="img" aria-label="Foto van een chalet"></div><div class="thumb-label">Kavel 24</div></div>
      <div class="pager"><span>&lt;&lt;</span><span>&gt;&gt;</span></div>
    </aside>
  </main>

  <footer class="site-footer">
    <div class="contact-line"><svg width="12" height="16" viewBox="0 0 12 16"><path fill="#fff" d="M6 0a6 6 0 0 0-6 6c0 4.5 6 10 6 10s6-5.5 6-10a6 6 0 0 0-6-6zm0 8.5A2.5 2.5 0 1 1 6 3.5a2.5 2.5 0 0 1 0 5z"/></svg>Wilgenlaan 14 1234 AB Dorpsveld</div>
    <div class="contact-line"><svg width="13" height="13" viewBox="0 0 24 24"><path fill="#fff" d="M6.6 10.8a15 15 0 0 0 6.6 6.6l2.2-2.2c.3-.3.7-.4 1-.2 1.1.4 2.3.6 3.6.6.6 0 1 .4 1 1V20c0 .6-.4 1-1 1C10.6 21 3 13.4 3 4c0-.6.4-1 1-1h3.5c.6 0 1 .4 1 1 0 1.3.2 2.5.6 3.6.1.3 0 .7-.2 1z"/></svg>0123 - 45 67 89</div>
    <div class="contact-line"><svg width="14" height="11" viewBox="0 0 14 11"><rect x="0.5" y="0.5" width="13" height="10" fill="none" stroke="#fff"/><path d="M0.5 0.5 7 6l6.5-5.5" fill="none" stroke="#fff"/></svg>info@parclindewaard.example</div>
    <div class="social"><span></span><span></span><span></span></div>
    <div class="copyright">Copyright 2018 | Parc Lindewaard</div>
  </footer>
</div>
</body>
</html>
```